TAVRO Capital Group LLC a High Risk Big Rewards company for Rich Young Entrepreneurs

We would like a very modern, powerful in the eyes of our customers, modern, minimalist feel, financial gain. this business card is for young Rich entrepreneurs who want to invest money into High Risk, Big Rewards Businesses. The card Should sell the business!! let your creativity go Wild! I pick most of the designers for this project because of your BOLD Designs, I would like this card to be Bold, Modern, Minimalist, use as many effects in your graphic Artist Mind, Do not let the Financial sound of this business to make you think Conservative that's the last thing we are! if you have a lot of money and you want to play a risky market call US
Updates

Project Deadline Extended
Reason: have not received, enough designs to choose 1st and second place, sure I have received over 100 designs but it seems most designers are submitting every card they have ever made before and calling it mine, please we are looking for fresh ideas please!

Target Market(s)

Private Risky Investors

Industry/Entity Type

Financial

Contact Information for Business Card

powerful in the eyes of our customers,modern, minimalist feel

Font styles to use
Other font styles liked:
• Modern feeling fonts

Requirements
Must have
• The Company Name is TAVRO Capital Group LLC and it must be on the CARD
• My Name, title, Cell , email
• Delvin Ashcroft G.E.D.
• Managing Member
• 555.038.6195
• delvin@tavrocapitalgroup.example
Nice to have
• try a black thick plastic card with round corners with Delvin Ashcroft GED (make sure GED is smaller than name) just on one side of the card, and my phone number with out the icons and email on the other side, this card should look like a exclusive credit card or exclusive VIP card, something you would never loose

```html
<!DOCTYPE html>
<html lang="en">
<head>
<meta charset="utf-8">
<title>TAVRO Capital Group LLC – Card</title>
<link href="https://fonts.googleapis.com/css2?family=Open+Sans:wght@300;400&display=swap" rel="stylesheet">
<style>
  :root {
    --page-bg: #ffffff;
    --card-black: #04030a;
    --silver-dark: #a8a8aa;
    --silver-mid: #c4c4c6;
    --silver-light: #e8e8ea;
    --silver-text: #d2d2d4;
    --silver-soft: #9c9ca0;
    --ink-grey: #2e2e30;
  }
  html, body {
    margin: 0;
    padding: 0;
    width: 1200px;
    height: 801px;
    overflow: hidden;
    background: var(--page-bg);
  }
  .canvas {
    position: relative;
    width: 1200px;
    height: 801px;
    background: var(--page-bg);
  }
  .card {
    position: absolute;
    left: 58px;
    top: 83px;
    width: 1087px;
    height: 637px;
    border-radius: 56px;
    background: var(--card-black);
    overflow: hidden;
    font-family: "Open Sans", sans-serif;
  }
  .company-name {
    position: absolute;
    left: 62px;
    top: 62px;
    margin: 0;
    font-weight: 400;
    font-size: 20px;
    letter-spacing: 4px;
    text-transform: uppercase;
    color: var(--silver-soft);
  }
  .brand-name {
    position: absolute;
    right: 102px;
    bottom: 335px;
    margin: 0;
    font-weight: 300;
    font-size: 170px;
    line-height: 1;
    letter-spacing: -4px;
    color: var(--silver-text);
  }
  .silver-band {
    position: absolute;
    left: 0;
    top: 285px;
    width: 100%;
    height: 127px;
    background: linear-gradient(90deg,
      var(--silver-dark) 0%,
      var(--silver-mid) 18%,
      var(--silver-light) 32%,
      var(--silver-mid) 52%,
      var(--silver-light) 82%,
      var(--silver-mid) 100%);
    display: flex;
    align-items: center;
    justify-content: center;
  }
  .email {
    font-weight: 300;
    font-size: 46px;
    color: var(--ink-grey);
  }
  .holder {
    position: absolute;
    left: 62px;
    bottom: 62px;
    margin: 0;
    color: var(--silver-text);
  }
  .holder-name {
    display: block;
    font-weight: 300;
    font-size: 34px;
    line-height: 1.2;
  }
  .holder-credential {
    font-size: 20px;
    margin-left: 6px;
  }
  .holder-title {
    display: block;
    font-weight: 400;
    font-size: 18px;
    letter-spacing: 3px;
    text-transform: uppercase;
    color: var(--silver-soft);
    margin-top: 6px;
  }
  .phone {
    position: absolute;
    right: 62px;
    bottom: 62px;
    margin: 0;
    font-weight: 300;
    font-size: 34px;
    letter-spacing: 2px;
    color: var(--silver-text);
  }
</style>
</head>
<body>
  <div class="canvas">
    <div class="card">
      <p class="company-name">TAVRO Capital Group LLC</p>
      <p class="brand-name">TAVRO</p>
      <div class="silver-band">
        <span class="email">delvin@tavrocapitalgroup.example</span>
      </div>
      <p class="holder">
        <span class="holder-name">Delvin Ashcroft<span class="holder-credential">G.E.D.</span></span>
        <span class="holder-title">Managing Member</span>
      </p>
      <p class="phone">555.038.6195</p>
    </div>
  </div>
</body>
</html>
```